Business Cards

I'd like help creating business cards with the full logo "Velmora Capital Partners" on the back of the card (navy background with white writing), and abbreviated logo "VCP" on the front. Would like to list name, title, phone number, email, and website listed on front of card. Would like to keep very simple. Front font Arial or similar.

```html
<!DOCTYPE html>
<html lang="en">
<head>
<meta charset="utf-8">
<title>Velmora Capital Partners – Business Cards</title>
<link href="https://fonts.googleapis.com/css2?family=Montserrat:wght@700&family=Arimo:wght@400;700&display=swap" rel="stylesheet">
<style>
  :root {
    --backdrop: #232323;
    --card-black: #1b1b1c;
    --navy: #22386f;
    --navy-bright: #243f86;
    --navy-deep: #1c3170;
    --white: #ffffff;
    --shadow: rgba(0, 0, 0, 0.55);
  }
  * { box-sizing: border-box; margin: 0; padding: 0; }
  html, body {
    width: 1200px;
    height: 780px;
    overflow: hidden;
    background: var(--backdrop);
  }
  .stage {
    position: relative;
    width: 1200px;
    height: 780px;
  }
  .card {
    position: absolute;
    top: 236px;
    width: 540px;
    height: 309px;
    overflow: hidden;
    box-shadow: 0 18px 40px var(--shadow);
  }

  /* Front card */
  .card-front {
    left: 40px;
    background: var(--card-black);
    font-family: Arimo, Arial, sans-serif;
  }
  .front-swoosh {
    position: absolute;
    inset: 0;
    width: 540px;
    height: 309px;
  }
  .front-monogram {
    position: absolute;
    left: 58px;
    top: 38px;
    display: flex;
    align-items: center;
    gap: 14px;
    font-family: Montserrat, Arial, sans-serif;
    font-weight: 700;
    font-size: 84px;
    line-height: 1;
    letter-spacing: 2px;
    color: var(--navy);
  }
  .front-person {
    position: absolute;
    left: 40px;
    top: 176px;
  }
  .person-name {
    font-weight: 700;
    font-size: 34px;
    color: var(--navy-bright);
    letter-spacing: 0.5px;
  }
  .person-title {
    margin-top: 6px;
    font-size: 16px;
    color: var(--white);
  }
  .front-divider {
    position: absolute;
    left: 292px;
    top: 52px;
    width: 2px;
    height: 96px;
    background: var(--white);
  }
  .contact-list {
    position: absolute;
    left: 312px;
    top: 52px;
    list-style: none;
  }
  .contact-item {
    display: flex;
    align-items: center;
    gap: 8px;
    height: 22px;
    font-size: 14px;
    color: var(--white);
  }
  .contact-icon {
    width: 13px;
    height: 13px;
    flex: none;
  }

  /* Back card */
  .card-back {
    left: 620px;
    background: var(--navy-deep);
  }
  .back-texture {
    position: absolute;
    inset: 0;
    background:
      radial-gradient(ellipse at 30% 35%, #26428a 0%, transparent 60%),
      linear-gradient(135deg, #213b80 0%, #1c3170 55%, #1a2d68 100%);
  }
  .back-wordmark {
    position: absolute;
    left: 0;
    right: 0;
    top: 92px;
    text-align: center;
    font-family: Montserrat, Arial, sans-serif;
    font-weight: 700;
    color: var(--white);
    line-height: 1;
  }
  .wordmark-main {
    display: block;
    font-size: 66px;
    letter-spacing: 3px;
  }
  .wordmark-sub {
    display: block;
    margin-top: 18px;
    font-size: 21px;
    letter-spacing: 11px;
    padding-left: 11px;
  }
</style>
</head>
<body>
<main class="stage">

  <section class="card card-front" aria-label="Business card front">
    <svg class="front-swoosh" viewBox="0 0 540 309" aria-hidden="true">
      <path d="M150 309 Q420 250 540 28 L540 309 Z" fill="var(--navy)"/>
      <path d="M70 302 Q400 238 522 6" fill="none" stroke="var(--navy)" stroke-width="3"/>
    </svg>

    <div class="front-monogram">VCP</div>

    <div class="front-person">
      <p class="person-name">Owen Hartley</p>
      <p class="person-title">Co-Founder and Managing Partner</p>
    </div>

    <div class="front-divider"></div>

    <ul class="contact-list">
      <li class="contact-item">
        <svg class="contact-icon" viewBox="0 0 24 24" aria-hidden="true"><path fill="var(--navy-bright)" d="M6.6 10.8a15 15 0 0 0 6.6 6.6l2.2-2.2a1 1 0 0 1 1-.25 11.4 11.4 0 0 0 3.6.57 1 1 0 0 1 1 1V20a1 1 0 0 1-1 1A17 17 0 0 1 3 4a1 1 0 0 1 1-1h3.5a1 1 0 0 1 1 1c0 1.25.2 2.45.57 3.57a1 1 0 0 1-.25 1z"/></svg>
        <span>(555) 014-2290</span>
      </li>
      <li class="contact-item">
        <svg class="contact-icon" viewBox="0 0 24 24" aria-hidden="true"><circle cx="12" cy="12" r="9" fill="none" stroke="var(--navy-bright)" stroke-width="2.4"/><path d="M3 12h18M12 3c3 3 3 15 0 18M12 3c-3 3-3 15 0 18" fill="none" stroke="var(--navy-bright)" stroke-width="1.8"/></svg>
        <span>www.velmoracp.com</span>
      </li>
      <li class="contact-item">
        <svg class="contact-icon" viewBox="0 0 24 24" aria-hidden="true"><rect x="2" y="5" width="20" height="14" rx="2" fill="var(--navy-bright)"/><path d="M3 6l9 7 9-7" fill="none" stroke="var(--card-black)" stroke-width="1.8"/></svg>
        <span>Owen.Hartley@VelmoraCP.com</span>
      </li>
    </ul>
  </section>

  <section class="card card-back" aria-label="Business card back">
    <div class="back-texture" role="img" aria-label="Subtle repeating embossed company-name pattern on navy"></div>
    <div class="back-wordmark">
      <span class="wordmark-main">VELMORA</span>
      <span class="wordmark-sub">CAPITAL PARTNERS</span>
    </div>
  </section>

</main>
</body>
</html>
```